Fern Hollow Academy business card

we need to incorporate our school logo, name, address onto a great new school business card for all our staff - I included a lot of detail below under must haves and I included 3 business card samples below also that give a flavour of what I want - I would like to include a great graphic on at least one side of the card that represents education -

Target Market(s)

this business card will need to be attractive to parents of all ages but especially millennial parents and even high school students who may influence parents to chose Fern Hollow Academy

Industry/Entity Type

Education

Contact Information for Business Card

should contain core value words "excellence service family belief"
will need out school name, Fern Hollow Academy to be present, address 7281 Marston Avenue, Burnaby, British Columbia V3K8P1
telephone 604.871.2960 Ext. 317
first card will need my name on it, Maribel Tansey, Director of Development & Operations
also web address of fernhollowacademy.ca

Font styles to use
Other font styles liked:
• Tw Cent MT

Requirements
Must have
• a fresh modern look for a private school environment that appeals to parents looking for great education - must use school logo, and incorporate colours navy blue, CMYK 100, 60, 0, 56 and burgundy CMYK 27, 98, 81, 50
• below I uploaded 3 business card layouts that look interesting to me - I'd like to incorporate some great school photos into the design - I tried to upload some school photos that we have, that the files are too large apparently? so I could send a link to Filecrate or something like that to share great high res pics that would look nice - we are kindergarten to Gr. 12 school, so I would like to include images that would represent great education at any age.
Nice to have
• spot colour would be nice as an option for printing for maybe key administrator business cards, while the rest would be basic printing

```html
<!DOCTYPE html>
<html lang="en">
<head>
<meta charset="utf-8">
<title>Fern Hollow Academy – Business Card</title>
<link href="https://fonts.googleapis.com/css2?family=Jost:wght@400;500;600;700&display=swap" rel="stylesheet">
<style>
  :root {
    --navy: #0b2f6f;
    --burgundy: #5d0a1d;
    --sky: #b9c8e1;
    --paper: #ffffff;
    --page: #ffffff;
  }
  * { box-sizing: border-box; margin: 0; padding: 0; }
  html, body {
    width: 1033px; height: 1200px; overflow: hidden;
    background: var(--page);
    font-family: "Jost", "Century Gothic", sans-serif;
  }
  .card { position: absolute; left: 29px; width: 975px; height: 556px; overflow: hidden; }
  .card--front { top: 31px; }
  .card--back { top: 607px; }

  .texture { position: absolute; inset: 0; background: linear-gradient(135deg, #f3f5f5, #e8ebeb); }

  .band { position: absolute; left: 0; width: 100%; height: 23px; display: flex; }
  .band--top { top: 0; }
  .band--bottom { bottom: 0; }
  .seg-burgundy { display: block; height: 100%; background: var(--burgundy); }
  .seg-navy { display: block; height: 100%; background: var(--navy); }

  .mark { position: absolute; border-radius: 50%; background: var(--navy); }
  .wordmark {
    position: absolute; color: var(--burgundy); font-weight: 700;
    text-transform: uppercase; line-height: 0.92; letter-spacing: -0.01em;
  }

  /* Front */
  .card--front .mark { left: 170px; top: 160px; width: 220px; height: 220px; }
  .card--front .wordmark { left: 430px; top: 150px; font-size: 92px; }
  .values {
    position: absolute; left: 434px; top: 418px;
    color: var(--navy); font-weight: 500; font-size: 18px;
    letter-spacing: 0.06em; text-transform: uppercase; white-space: nowrap;
  }

  /* Back header */
  .header { position: absolute; left: 0; top: 0; width: 100%; height: 198px; background: var(--paper); }
  .rule { position: absolute; left: 0; top: 198px; width: 100%; height: 15px; display: flex; }
  .card--back .mark { left: 52px; top: 36px; width: 126px; height: 126px; }
  .card--back .wordmark { left: 196px; top: 44px; font-size: 40px; }

  .person { position: absolute; right: 42px; top: 40px; text-align: right; text-transform: uppercase; }
  .person__name { color: var(--navy); font-weight: 600; font-size: 52px; line-height: 1; letter-spacing: -0.01em; white-space: nowrap; }
  .person__role { color: var(--sky); font-weight: 500; font-size: 27px; line-height: 1.1; margin-top: 8px; }

  /* Back contacts */
  .contacts { position: absolute; left: 60px; top: 262px; list-style: none; }
  .contact { display: flex; align-items: center; height: 66px; margin-bottom: 18px; }
  .contact__icon {
    width: 66px; height: 66px; border-radius: 50%; background: var(--navy);
    display: flex; align-items: center; justify-content: center; flex: none;
  }
  .contact__text {
    margin-left: 24px; color: var(--burgundy); font-weight: 500; font-size: 29px;
    text-transform: uppercase; letter-spacing: -0.01em; white-space: nowrap;
  }
</style>
</head>
<body>

<section class="card card--front" aria-label="Card front">
  <div class="texture" role="img" aria-label="Soft light grey geometric background texture"></div>
  <div class="band band--top">
    <span class="seg-burgundy" style="width:118px"></span>
    <span class="seg-navy" style="width:737px"></span>
    <span class="seg-burgundy" style="width:120px"></span>
  </div>
  <div class="mark"></div>
  <div class="wordmark">Fern<br>Hollow<br>Academy</div>
  <p class="values">Excellence · Service · Family · Belief</p>
  <div class="band band--bottom">
    <span class="seg-burgundy" style="width:118px"></span>
    <span class="seg-navy" style="width:737px"></span>
    <span class="seg-burgundy" style="width:120px"></span>
  </div>
</section>

<section class="card card--back" aria-label="Card back">
  <div class="texture" role="img" aria-label="Soft light grey geometric background texture"></div>
  <header class="header">
    <div class="mark"></div>
    <div class="wordmark">Fern<br>Hollow<br>Academy</div>
    <div class="person">
      <p class="person__name">Maribel Tansey</p>
      <p class="person__role">Director of Development<br>&amp; Operations</p>
    </div>
  </header>
  <div class="rule">
    <span class="seg-navy" style="width:476px"></span>
    <span class="seg-burgundy" style="width:499px"></span>
  </div>

  <ul class="contacts">
    <li class="contact">
      <span class="contact__icon">
        <svg width="30" height="40" viewBox="0 0 30 40" aria-hidden="true">
          <path d="M15 2C8 2 3 7 3 14c0 9 12 24 12 24s12-15 12-24C27 7 22 2 15 2z" fill="#fff"/>
          <circle cx="15" cy="14" r="5" fill="var(--navy)"/>
        </svg>
      </span>
      <span class="contact__text">7281 Marston Avenue, Burnaby, BC V3K8P1</span>
    </li>
    <li class="contact">
      <span class="contact__icon">
        <svg width="38" height="38" viewBox="0 0 38 38" aria-hidden="true" fill="none" stroke="#fff" stroke-width="3">
          <circle cx="19" cy="19" r="15"/>
          <ellipse cx="19" cy="19" rx="6.5" ry="15"/>
          <path d="M4 19h30M7 11h24M7 27h24"/>
        </svg>
      </span>
      <span class="contact__text">fernhollowacademy.ca</span>
    </li>
    <li class="contact">
      <span class="contact__icon">
        <svg width="40" height="34" viewBox="0 0 40 34" aria-hidden="true">
          <path d="M3 12c0-5 6-8 17-8s17 3 17 8v3h-8v-4c-3-1-6-1.5-9-1.5S14 10 11 11v4H3z" fill="#fff"/>
          <path d="M9 17h22l4 14H5z" fill="#fff"/>
          <circle cx="20" cy="24" r="4" fill="var(--navy)"/>
        </svg>
      </span>
      <span class="contact__text">604.871.2960 Ext. 317</span>
    </li>
  </ul>
</section>

</body>
</html>
```